Solar Flyer-Design
Zielgruppe
Quornel Energie
Für die Firma QuorNel Energie wird ein Flyer im Wickel oder Zickzackfalz Design benötigt. Größe soll Din Lang sein mit insgesamt 6 Seiten.
Es sollen die Inhalte der Webseite (quornel-energie.de bestmöglich verwendet werden.
Aufgabenstellung
Design anhand der Webseite, Bilder auch von der Webseite.
Logo befindet sich im Anhang und Bilder können frei von der Webseite genommen werden, wir besitzen alle Lizenzen daran.

```html
<!DOCTYPE html>
<html lang="de">
<head>
<meta charset="utf-8">
<title>Quornel Energie – Flyer DIN Lang</title>
<link href="https://fonts.googleapis.com/css2?family=Montserrat:wght@400;500;600;700;800&display=swap" rel="stylesheet">
<style>
:root{
  --stage:#e9eaec;
  --sky-top:#cfe7f8;
  --sky-bottom:#f4f9fd;
  --blue:#1e9be6;
  --navy:#1f3f80;
  --ink:#2b2f36;
  --green:#93c024;
  --orange:#f28c12;
  --white:#ffffff;
  --grass:#6fae2f;
}
*{box-sizing:border-box;margin:0;padding:0}
html,body{width:898px;height:1200px;overflow:hidden}
body{background:var(--stage);font-family:'Montserrat',sans-serif;color:var(--ink);position:relative}
.sheet{position:absolute;left:70px;width:759px;height:536px;display:grid;
  background:linear-gradient(180deg,var(--sky-top) 0%,var(--sky-bottom) 55%,var(--white) 100%);overflow:hidden}
.sheet--outside{top:48px;grid-template-columns:249px 262px 248px}
.sheet--inside{top:616px;grid-template-columns:255px 256px 248px}
.panel{position:relative;border-right:1px solid rgba(0,0,0,.06)}
.panel:last-child{border-right:none}
.ph{position:absolute}
.head-box{background:var(--blue);color:var(--white);font-weight:800;text-transform:uppercase;position:relative;z-index:2}
.head-box::after{content:"";position:absolute;bottom:-8px;right:22px;border-left:9px solid transparent;border-right:9px solid transparent;border-top:8px solid var(--blue)}
.head-box.green{background:var(--green)}
.head-box.green::after{border-top-color:var(--green)}
.body{font-size:7.2px;line-height:1.6;font-weight:500}
.body p+p{margin-top:8px}
.brand{font-weight:800;color:var(--ink);letter-spacing:.5px;text-align:center;display:flex;align-items:center;justify-content:center;gap:6px}
.brand .dot{width:9px;height:9px;background:var(--green);display:inline-block}

/* outside */
.o1 .head-box{padding:17px 16px 0 16px;font-size:11.8px;line-height:1.2;height:90px}
.o1 .roof{left:38px;top:84px;width:196px;height:70px;background:linear-gradient(180deg,#4a6fb8 0%,#2e56a6 60%,#c0553a 100%)}
.o1 .body{position:absolute;left:15px;right:15px;top:184px;font-size:6.9px}
.o1 .note{position:absolute;left:15px;right:15px;top:282px;height:95px;background:var(--navy);color:var(--white);padding:15px 18px;font-size:6.9px;line-height:1.5;font-weight:500}
.o1 .note p+p{margin-top:10px}
.o1 .illu{left:26px;top:388px;width:192px;height:84px;background:linear-gradient(135deg,#f6c64b 0%,#4f9be0 55%,#8cc44a 100%);opacity:.85}
.o2 .services{position:absolute;top:72px;left:0;right:0;text-align:center;color:var(--navy);font-size:7.6px;font-weight:600;line-height:1.35;text-transform:uppercase}
.o2 .services li{list-style:none;margin-bottom:12px}
.o2 .brand{position:absolute;top:252px;left:0;right:0;font-size:18px}
.o2 .url{position:absolute;top:308px;left:0;right:0;text-align:center;font-size:9px;font-weight:500}
.o3 .brand{position:absolute;top:44px;left:0;right:0;font-size:19px}
.o3 .title{position:absolute;top:112px;left:4px;right:4px;text-align:center;color:var(--navy);font-weight:800;font-size:16.2px;line-height:1.22;text-transform:uppercase}
.o3 .ask{position:absolute;top:224px;left:47px;width:154px;height:80px;background:var(--green);color:var(--white);text-align:right;padding:14px 8px 0 8px;font-size:9.4px;line-height:1.3;font-weight:500;z-index:2}
.o3 .ask::before{content:"";position:absolute;top:4px;right:10px;border-left:5px solid transparent;border-right:5px solid transparent;border-top:5px solid var(--white)}
.house{position:absolute;left:266px;top:290px;width:493px;height:184px;background:linear-gradient(180deg,#5e8fcf 0%,#2a4f8c 45%,#1e3a6f 100%)}
.grass{position:absolute;left:0;right:0;bottom:0;height:64px;background:linear-gradient(180deg,#9fd055 0%,var(--grass) 100%)}

/* inside */
.i1 .head-box,.i3 .head-box.top{padding:25px 18px 0 18px;font-size:11.8px;line-height:1.2;height:84px}
.i1 .illu{left:26px;top:92px;width:184px;height:124px;background:linear-gradient(180deg,#fde9a8 0%,#cfe1f1 40%,#3a4f7c 70%,#e9eef3 100%);opacity:.8}
.i1 .body{position:absolute;left:20px;right:12px;top:224px;font-size:7.2px}
.i1 .highlight{color:var(--blue);font-weight:800;text-transform:uppercase;font-size:7.1px;line-height:1.6}
.i1 .city{left:26px;top:394px;width:200px;height:126px;background:linear-gradient(180deg,#cde4f3 0%,#f7c24a 45%,#4e86c9 75%,#6ba838 100%);opacity:.8}
.i2 .illu{left:27px;top:16px;width:208px;height:124px;background:linear-gradient(180deg,#d7ebf8 0%,#f4d06a 45%,#8cc44a 80%,#e7f2fb 100%);opacity:.85}
.i2 .head-box.green{position:absolute;top:160px;left:0;right:0;height:44px;padding:9px 14px 0;font-size:11.4px;line-height:1.2}
.i2 .intro{position:absolute;top:220px;left:14px;right:14px;font-size:7.1px}
.i2 .reasons{position:absolute;top:266px;left:0;right:0;height:198px;background:var(--orange);color:var(--white);padding:10px 12px}
.i2 .reasons h3{font-size:9.4px;font-weight:800;text-transform:uppercase;margin-bottom:5px}
.i2 .reasons li{list-style:none;display:flex;gap:5px;font-size:6.3px;line-height:1.35;font-weight:600;margin-bottom:5.2px}
.i2 .reasons svg{flex:0 0 7px;margin-top:1px}
.i2 .foot{position:absolute;top:474px;left:14px;right:14px;font-size:5.6px;line-height:1.6}
.i2 .foot b{font-weight:700}
.i3 .head-box.top{padding-left:20px}
.i3 .body{position:absolute;left:19px;right:14px;top:108px;font-size:7.2px}
.i3 .body b{font-weight:700}
.surfaces{position:absolute;top:262px;left:14px;right:14px;display:grid;grid-template-columns:repeat(4,1fr)}
.surfaces div,.factors div{text-align:center;font-size:4.8px;font-weight:600;text-transform:uppercase}
.surfaces div+div{border-left:1px solid #cfd6de}
.icon{display:block;margin:0 auto 3px;width:22px;height:24px;background:linear-gradient(180deg,#f2a33a,#3a5f95);opacity:.85}
.i3 .head-box.green{position:absolute;top:322px;left:0;right:0;height:56px;padding:9px 14px 0 14px;font-size:11.4px;line-height:1.2}
.factors{position:absolute;top:396px;left:14px;right:14px;display:grid;grid-template-columns:repeat(3,1fr);row-gap:12px}
.factors .icon{width:30px;height:30px;background:linear-gradient(180deg,#f6c64b,#3b7fc9)}
.i3 .band{position:absolute;left:0;right:0;bottom:0;height:12px;background:var(--blue)}
</style>
</head>
<body>

<section class="sheet sheet--outside">
  <div class="panel o1">
    <h2 class="head-box">Die Erträge fallen niedriger aus, wenn die Dachneigung unter 35 Grad und über 40 Grad liegt.</h2>
    <div class="ph roof" role="img" aria-label="Foto: Ziegeldach mit Solarmodulen"></div>
    <div class="body">
      <p>Eine Dachneigung von 35 bis 40 Grad ist optimal für hohe Erträge. Auf Flachdächern kann eine Aufständerung der Photovoltaik Module erfolgen.</p>
      <p>Eine Montage der Module an der Fassade ist möglich, wenn die Sonneneinstrahlung an der Fassade entsprechend hoch ist. Die Erträge liegen allerdings deutlich niedriger als bei der Dachmontage.</p>
    </div>
    <div class="note">
      <p>Wir installieren Photovoltaik-Anlagen mit einer Leistung von bis zu 30 kWp für Privatkunden.</p>
      <p>Für gewerbliche Kundeninstallieren wir Photovoltaik-Anlagen mit einer Leistung von bis zu 500 kWp.</p>
    </div>
    <div class="ph illu" role="img" aria-label="Illustration: zwei Personen an Solarmodulen mit Glühbirne"></div>
  </div>
  <div class="panel o2">
    <ul class="services">
      <li>Intelligentes<br>Energie-Management</li>
      <li>Alle Leistungen<br>aus einer Hand</li>
      <li>Notstromfähige Wechselrichter<br>und Insellösungen</li>
      <li>Hochwertige Photovoltaik<br>Module aus der EU</li>
    </ul>
    <div class="brand"><span class="dot"></span>Quornel Energie</div>
    <div class="url">quornel-energie.de</div>
  </div>
  <div class="panel o3">
    <div class="brand"><span class="dot"></span>Quornel Energie</div>
    <h1 class="title">Saubere Stromerzeugung mithilfe von einer Photovoltaik-Anlage.</h1>
    <div class="ask">Möchtest Du Deinen eigenen Strom erzeugen und unabhängiger werden?</div>
  </div>
  <div class="house" role="img" aria-label="Foto: blaues Haus mit Solardach und Solarfeld"></div>
  <div class="grass" role="img" aria-label="Foto: grüne Wiese"></div>
</section>

<section class="sheet sheet--inside">
  <div class="panel i1">
    <h2 class="head-box">Photovoltaikanlage eine saubere und umweltfreundliche Lösung.</h2>
    <div class="ph illu" role="img" aria-label="Illustration: Haus mit Solardach, Sonne und Person"></div>
    <div class="body">
      <p>Bei uns als Full-Service-Anbieter für PV-Anlagen, für private und gewerbliche Kunden, bist Du an der richtigen Adresse. Gemeinsam mit uns kannst Du Deine PV Anlage planen, abhängig von den örtlichen Gegebenheiten und Deinem Stromverbrauch.</p>
      <p class="highlight">Den erzeugten Strom kannst Du selbst nutzen, um Stromkosten zu sparen und/oder ihn an den örtlichen Stromnetzbetreiber verkaufen.</p>
      <p>Mit einer vollumfänglichen PV-Anlage (z.B. mit einem Speicher) senkst Du deine Energiekosten.</p>
    </div>
    <div class="ph city" role="img" aria-label="Illustration: Stadt mit Fabrik und Solarpark"></div>
  </div>
  <div class="panel i2">
    <div class="ph illu" role="img" aria-label="Illustration: Haus mit Solardach, Elektroauto und Batterie"></div>
    <h2 class="head-box green">Selbst zum Stromerzeuger werden mit der</h2>
    <p class="body intro">Du hast ein Eigenheim und/oder besitzt Immobilien mit genügend Platz auf dem Dach, dann ist eine Photovoltaik-Anlage eine gute Option.</p>
    <div class="reasons">
      <h3>Dafür gibt es mehrere gute Gründe:</h3>
      <ul>
        <li><svg width="7" height="7" viewBox="0 0 7 7"><rect width="7" height="7" fill="#fff"/><path d="M1.3 3.6 2.9 5.1 5.8 1.8" stroke="#f28c12" stroke-width="1.2" fill="none"/></svg>Du wirst unabhängiger von den öffentlichen Stromanbietern</li>
        <li><svg width="7" height="7" viewBox="0 0 7 7"><rect width="7" height="7" fill="#fff"/><path d="M1.3 3.6 2.9 5.1 5.8 1.8" stroke="#f28c12" stroke-width="1.2" fill="none"/></svg>Du leistest einen Beitrag zur Energiewende und zum Klimaschutz</li>
        <li><svg width="7" height="7" viewBox="0 0 7 7"><rect width="7" height="7" fill="#fff"/><path d="M1.3 3.6 2.9 5.1 5.8 1.8" stroke="#f28c12" stroke-width="1.2" fill="none"/></svg>Photovoltaik ist eine saubere Form der Energieerzeugung, da keine Schadstoffe ausgestoßen werden</li>
        <li><svg width="7" height="7" viewBox="0 0 7 7"><rect width="7" height="7" fill="#fff"/><path d="M1.3 3.6 2.9 5.1 5.8 1.8" stroke="#f28c12" stroke-width="1.2" fill="none"/></svg>Einspeisevergütung wird gezahlt, wenn der Strom in ein öffentliches Netz verkauft wird</li>
        <li><svg width="7" height="7" viewBox="0 0 7 7"><rect width="7" height="7" fill="#fff"/><path d="M1.3 3.6 2.9 5.1 5.8 1.8" stroke="#f28c12" stroke-width="1.2" fill="none"/></svg>Du sparst Stromkosten, wenn Du den Strom selbst nutzt</li>
        <li><svg width="7" height="7" viewBox="0 0 7 7"><rect width="7" height="7" fill="#fff"/><path d="M1.3 3.6 2.9 5.1 5.8 1.8" stroke="#f28c12" stroke-width="1.2" fill="none"/></svg>Eine PV Anlage kann mit Elektromobilität kombiniert werden</li>
        <li><svg width="7" height="7" viewBox="0 0 7 7"><rect width="7" height="7" fill="#fff"/><path d="M1.3 3.6 2.9 5.1 5.8 1.8" stroke="#f28c12" stroke-width="1.2" fill="none"/></svg>PV-Anlagen kommen mit wenig Wartung aus</li>
        <li><svg width="7" height="7" viewBox="0 0 7 7"><rect width="7" height="7" fill="#fff"/><path d="M1.3 3.6 2.9 5.1 5.8 1.8" stroke="#f28c12" stroke-width="1.2" fill="none"/></svg>Lebensdauer einer PV-Anlage liegt bei ca. 20 bis 25 Jahren</li>
        <li><svg width="7" height="7" viewBox="0 0 7 7"><rect width="7" height="7" fill="#fff"/><path d="M1.3 3.6 2.9 5.1 5.8 1.8" stroke="#f28c12" stroke-width="1.2" fill="none"/></svg>Förderung für die Errichtung von PV-Anlagen ist möglich</li>
      </ul>
    </div>
    <p class="foot">Die Einsparung pro Kilowattstunde Strom aus der PV-Anlage, den Du selbst nutzt, ist deutlich höher als die zu erwartende Einspeisevergütung. <b>Entscheidest Du Dich für eine vollumfängliche PV-Anlage mit Speicher, so kannst Du deinen Strombedarf selbst erzeugen,</b> Speichern und den Strom auch dann nutzen, wenn die Sonne nicht scheint.</p>
  </div>
  <div class="panel i3">
    <h2 class="head-box top">Die Installation von Photovoltaikanlagen auf verschiedenen Flächen</h2>
    <div class="body">
      <p>Eine Photovoltaikanlage kann nicht nur auf dem Dach Deines Hauses installiert werden, sondern auch auf Garagen, Carports Industriedächern und Freiflächen. So lassen sich komplette Solarparks errichten. Die PV-Modul Dachmontage sollte so erfolgen, dass die Erträge an Strom möglichst hoch sind.</p>
      <p><b>Optimal ist ein Dach mit Südausrichtung, doch geeignet sind auch Dächer mit Südwest-, Südost- und Ostwest Ausrichtung, allerdings fallen die Erträge dann geringer aus.</b></p>
    </div>
    <div class="surfaces">
      <div><span class="icon" role="img" aria-label="Symbol Garage"></span>Garage</div>
      <div><span class="icon" role="img" aria-label="Symbol Dächer"></span>Dächer</div>
      <div><span class="icon" role="img" aria-label="Symbol Carport"></span>Carport</div>
      <div><span class="icon" role="img" aria-label="Symbol Industrieflächen"></span>Industrieflächen</div>
    </div>
    <h2 class="head-box green">Die Energieerzeugungserträge hängen von verschiedenen Faktoren ab:</h2>
    <div class="factors">
      <div><span class="icon" role="img" aria-label="Symbol Kompass"></span>Ausrichtung<br>des Daches</div>
      <div><span class="icon" role="img" aria-label="Symbol Dachneigung"></span>Dachneigung</div>
      <div><span class="icon" role="img" aria-label="Symbol Wetter"></span>Witterung</div>
      <div><span class="icon" role="img" aria-label="Symbol Sonne über Modulen"></span>Sonneneinstrahlung</div>
      <div><span class="icon" role="img" aria-label="Symbol Karte mit Markierung"></span>Region</div>
      <div><span class="icon" role="img" aria-label="Symbol Baum mit Schatten"></span>Beschattung</div>
    </div>
    <div class="band"></div>
  </div>
</section>

</body>
</html>
```